IT NETWORK INTEGRATION Brochure Design Project

Hi. i am placing a request for a new brochure design for our company: VENTRIX P/L. We will also be revamping our website with a totally new look and feel so please do not be influenced by our current website. I will be attaching files depicting our business card theme which should be somehow followed through your design process. We are in the business of providing Data Network Integration at both LAN and WAN levels, IT Security with EAL4+ assured appliances, Cloud, Sever and Desktop Virtualisation, Video Conferencing, etc

We need a brochure that is absolutely professional, catchy and informative on the services we offer plus information on the company, business and goals - a very impressive information brochure to be used for every client introduction and initiative.
Updates

Industry/Entity Type

Business

Requirements
Must have
• Common pattern of company presence on every page, though the page can have a separate design or color code service wise.

```html
<!DOCTYPE html>
<html lang="en">
<head>
<meta charset="utf-8">
<title>VENTRIX P/L — Network Integration Brochure</title>
<link rel="stylesheet" href="https://fonts.googleapis.com/css2?family=Libre+Baskerville:wght@700&family=Noto+Sans:wght@400;700&family=PT+Sans:wght@400;700&display=swap">
<style>
  :root {
    --backdrop: #e6e6e6;
    --cream: #ece6d6;
    --olive: #8c9a44;
    --olive-dark: #6f7d30;
    --khaki: #b9a555;
    --khaki-text: #8a7a3a;
    --white: #ffffff;
    --ink: #2b2b2b;
    --pattern-a: #9fae6a;
    --pattern-b: #dcd5bf;
    --photo-a: #9aa36a;
    --photo-b: #3f4622;
  }
  * { margin: 0; padding: 0; box-sizing: border-box; }
  html, body { width: 1200px; height: 838px; overflow: hidden; background: var(--backdrop); }
  .canvas {
    width: 1200px; height: 838px; position: relative;
    display: grid; grid-template-columns: 390px 390px; grid-template-rows: 390px 390px;
    gap: 30px; justify-content: center; align-content: center;
  }
  .page {
    position: relative; width: 390px; height: 390px; overflow: hidden;
    box-shadow: 0 4px 12px rgba(0,0,0,.25);
  }
  .page-art { position: absolute; inset: 0; width: 390px; height: 390px; }

  /* Cover */
  .cover { background: var(--cream); }
  .cover-pattern {
    position: absolute; left: 0; top: 0; width: 200px; height: 150px;
    background: linear-gradient(135deg, var(--pattern-a) 0%, #c4cb9a 45%, var(--pattern-b) 100%);
    -webkit-mask: linear-gradient(160deg, #000 40%, transparent 95%);
            mask: linear-gradient(160deg, #000 40%, transparent 95%);
  }
  .cover-title {
    position: absolute; left: 22px; top: 180px; width: 350px;
    font-family: "Noto Sans", sans-serif; font-weight: 700; color: var(--khaki-text);
    line-height: 1.05;
  }
  .cover-title .small { font-size: 9px; }
  .cover-title .big { font-size: 17px; }
  .cover-title .line2 { display: block; padding-left: 60px; }
  .cover-brand {
    position: absolute; right: 24px; bottom: 24px; width: 72px; height: 72px;
    background: linear-gradient(160deg, #b6c27a, var(--olive));
    display: flex; align-items: flex-end; justify-content: center; padding-bottom: 8px;
  }
  .brand-name {
    font-family: "Noto Sans", sans-serif; font-weight: 700; font-size: 10px;
    color: var(--white); letter-spacing: .04em;
  }

  /* Inner pages */
  .inner { background: var(--white); }
  .page-heading {
    position: absolute; top: 26px; display: flex; align-items: center; gap: 6px;
    font-family: "Libre Baskerville", serif; font-weight: 700; font-size: 10px; color: var(--olive-dark);
  }
  .inner-left .page-heading { left: 48px; }
  .inner-right .page-heading { left: 20px; }
  .heading-mark { width: 11px; height: 11px; background: var(--olive); border: 1.5px solid var(--white); outline: 1px solid var(--olive); }
  .heading-dots {
    position: absolute; top: 44px; height: 3px; width: 150px;
    background: radial-gradient(circle, var(--olive) 1.2px, transparent 1.5px) 0 0 / 10px 3px repeat-x;
  }
  .inner-left .heading-dots { left: 64px; }
  .inner-right .heading-dots { left: 36px; }
  .copy {
    position: absolute; font-family: "PT Sans", sans-serif; font-size: 8px;
    line-height: 1.35; color: var(--ink); text-align: justify;
  }
  .copy p + p { margin-top: 4px; }
  .photo {
    position: absolute; left: 137px; top: 148px; width: 116px; height: 116px; border-radius: 50%;
    background: radial-gradient(circle at 40% 35%, var(--photo-a), var(--photo-b));
    border: 3px solid var(--white); box-shadow: 0 0 0 1px #c9cca8;
  }

  /* Back */
  .back { background: var(--white); }
  .back-brand {
    position: absolute; left: 155px; top: 130px; width: 80px;
    display: flex; flex-direction: column; align-items: center; gap: 8px;
  }
  .back-brand-square { width: 64px; height: 64px; background: var(--white); }
  .back-contact {
    position: absolute; left: 145px; top: 270px; width: 100px; text-align: center;
    font-family: "PT Sans", sans-serif; font-size: 7px; line-height: 1.4; color: var(--white);
  }
</style>
</head>
<body>
<main class="canvas">

  <section class="page cover">
    <div class="cover-pattern" role="img" aria-label="Mosaic of rounded squares in olive and cream tones"></div>
    <h1 class="cover-title">
      <span class="small">When Your</span> <span class="big">Network</span>
      <span class="line2"><span class="small">Needs to be</span> <span class="big">Efficient</span> <span class="small">and</span> <span class="big">Effective</span></span>
    </h1>
    <div class="cover-brand"><span class="brand-name">VENTRIX</span></div>
  </section>

  <section class="page inner inner-left">
    <svg class="page-art" viewBox="0 0 390 390" aria-hidden="true">
      <rect width="390" height="390" fill="var(--olive)"/>
      <path d="M0 80 C0 38 30 18 90 18 H390 V390 H0 Z" fill="var(--white)"/>
      <path d="M0 300 C40 330 110 360 190 390 H0 Z" fill="var(--khaki)"/>
    </svg>
    <h2 class="page-heading"><span class="heading-mark"></span>When Our Network Meets Yours</h2>
    <div class="heading-dots"></div>
    <div class="copy" style="left:24px; top:60px; width:165px;">
      <p>We design and connect data networks across local and wide areas, so every office shares one secure and steady backbone.</p>
    </div>
    <div class="copy" style="left:205px; top:60px; width:165px;">
      <p>Our engineers plan, install and support each link, switch and router, keeping downtime low and growth simple.</p>
    </div>
    <div class="copy" style="left:24px; top:165px; width:105px;">
      <p>Security appliances with assured ratings guard the edge of your network and watch traffic around the clock.</p>
    </div>
    <div class="photo" role="img" aria-label="Photo of network hardware and cabling"></div>
    <div class="copy" style="left:262px; top:170px; width:108px;">
      <p>Every project starts with a clear review of your sites, users and goals.</p>
    </div>
    <div class="copy" style="left:150px; top:285px; width:220px;">
      <p>From first survey to final handover, one team stays with you, documents every change and trains your staff to run the network with confidence.</p>
    </div>
  </section>

  <section class="page inner inner-right">
    <svg class="page-art" viewBox="0 0 390 390" aria-hidden="true">
      <rect width="390" height="390" fill="var(--olive)"/>
      <path d="M0 18 H300 C360 18 390 38 390 80 V390 H0 Z" fill="var(--white)"/>
    </svg>
    <h2 class="page-heading"><span class="heading-mark"></span>When Our Network Meets Yours</h2>
    <div class="heading-dots"></div>
    <div class="copy" style="left:20px; top:60px; width:165px;">
      <p>Cloud, server and desktop virtualisation lets you do more with less hardware and move faster when demand shifts.</p>
    </div>
    <div class="copy" style="left:201px; top:60px; width:165px;">
      <p>We size each platform to your workload and keep it patched and backed up.</p>
    </div>
    <div class="copy" style="left:20px; top:165px; width:108px;">
      <p>Video conferencing rooms bring distant teams together with clear sound and sharp pictures.</p>
    </div>
    <div class="photo" role="img" aria-label="Photo of a clock face close up"></div>
    <div class="copy" style="left:262px; top:170px; width:108px;">
      <p>Our support desk answers fast and fixes issues before they reach your users.</p>
    </div>
    <div class="copy" style="left:20px; top:285px; width:230px;">
      <p>Talk to us about a network that fits your business today and grows with it tomorrow, backed by people who know your systems well.</p>
    </div>
  </section>

  <section class="page back">
    <svg class="page-art" viewBox="0 0 390 390" aria-hidden="true">
      <path d="M150 0 H390 V390 H60 C25 390 0 365 0 330 V170 C0 70 60 0 150 0 Z" fill="var(--khaki)"/>
    </svg>
    <div class="back-brand">
      <div class="back-brand-square"></div>
      <span class="brand-name">VENTRIX</span>
    </div>
    <address class="back-contact">Address<br>Phone<br>Website<br>email address</address>
  </section>

</main>
</body>
</html>
```